Book cover: Muddling Through Small Years (A5)

I have a book called Muddling Through Big Years. It is a book for teenagers which gives them tips and tactics on how to survive life's challenges regarding friends, family, feelings, relationships and hard stuff in life generally. I will upload the cover of this book but you can see it on my past jobs as one of the designers her eon Pixel Harbor did it for me.
I have a new book I've written called Muddling Through Small Years. This is a parallel book to Muddling Through Big Years, but it is specifically for 8 to 12 or 13 year olds, rather than for older teens.
A very important aspect of this job is that it SHOULD MATCH in some strong way - the Muddling Through Big Years book. I will be selling them together, displaying them together and I want them to look like two of a pair. It might be that you use the same image as the first book but change the colour of the image so that it is bright orange and green perhaps? Or that there is another image but in the image is placed in the exact same position across the book as the first book. It needs to look like the books are by the same author.
However, I would like this one to look a bit "younger", more kid friendly. For example, a font that looks like it is for kids, or kids' writing perhaps.
I dont want to have photos on the book, and I dont think I want cartoons or drawings - because I'm not sure how this will tie in with the first book.
I want it to look modern, fresh and designed specifically for kids. The text needs to be:
Muddling Through - Small Years!
Tips and ideas for 8 to 13 year olds about how to stay cool, calm and confident on even the toughest days!
The back cover is going to mostly just have the table of contents listed and a blurb, with one or two cartoons which I will supply. I am keen to pick a designer to just do the front cover first and will ask them to do the back cover later.
UPDATED: I have attached three files with fonts that I like.

```html
<!DOCTYPE html>
<html lang="en">
<head>
<meta charset="utf-8">
<title>Muddling Through - Small Years! — Front Cover</title>
<link rel="stylesheet" href="https://fonts.googleapis.com/css2?family=Great+Vibes&family=Raleway:wght@300;400&family=Roboto+Condensed:wght@400;700&display=swap">
<style>
  :root {
    --page-bg: #f2f1ef;
    --cover-white: #ffffff;
    --title-red: #c0242f;
    --band-red: #c8202c;
    --coral: #ef6a55;
    --blush: #f9c9bb;
    --deep-red: #9e1f26;
    --wine: #5a1e2a;
    --lavender: #9fa6d4;
    --panel-fill: rgba(48, 20, 26, 0.82);
    --panel-edge: #e9cfc4;
    --text-light: #ffffff;
  }
  * { margin: 0; padding: 0; box-sizing: border-box; }
  html, body {
    width: 1200px; height: 1000px; overflow: hidden;
    background: var(--page-bg);
  }
  .cover {
    position: absolute; left: 282px; top: 50px;
    width: 636px; height: 900px;
    background: var(--cover-white);
    overflow: hidden;
    box-shadow: 0 8px 30px rgba(0,0,0,0.18);
  }
  .pattern { position: absolute; display: block; }
  .pattern--top {
    left: 330px; top: 0; width: 306px; height: 190px;
    background: linear-gradient(200deg, var(--blush) 0%, rgba(249,201,187,0) 75%);
  }
  .pattern--accent {
    left: 120px; top: 40px; width: 110px; height: 70px;
    background: linear-gradient(135deg, var(--coral), rgba(239,106,85,0));
  }
  .pattern--lower { left: 0; top: 300px; width: 636px; height: 600px; }
  .title {
    position: absolute; left: 0; top: 90px; width: 636px;
    text-align: center; color: var(--title-red);
  }
  .title__lead {
    display: block;
    font-family: "Great Vibes", cursive;
    font-size: 78px; line-height: 1;
  }
  .title__main {
    display: block;
    font-family: "Great Vibes", cursive;
    font-size: 128px; line-height: 1; margin-top: -6px;
  }
  .title__sub {
    display: block;
    font-family: "Raleway", sans-serif; font-weight: 400;
    font-size: 46px; line-height: 1.1; margin-top: -4px;
  }
  .tagline-panel {
    position: absolute; left: 150px; top: 400px;
    width: 400px; height: 300px;
  }
  .tagline-panel svg { position: absolute; inset: 0; }
  .tagline {
    position: absolute; left: 60px; top: 82px; width: 280px;
    font-family: "Raleway", sans-serif; font-weight: 400;
    font-size: 21px; line-height: 1.3;
    color: var(--text-light); text-align: center;
  }
  .author-band {
    position: absolute; right: 0; top: 730px;
    width: 430px; height: 48px;
    background: var(--band-red);
    display: flex; align-items: center; gap: 10px;
    padding-left: 22px;
    font-family: "Roboto Condensed", sans-serif;
    color: var(--text-light);
  }
  .author-band__name { font-weight: 700; font-size: 28px; }
  .author-band__role { font-weight: 400; font-size: 19px; }
  .illustrator {
    position: absolute; right: 30px; top: 800px;
    font-family: "Roboto Condensed", sans-serif; font-weight: 400;
    font-size: 15px; color: var(--text-light);
  }
</style>
</head>
<body>
  <main class="cover">
    <div class="pattern pattern--top" role="img" aria-label="Faint geometric triangle pattern in blush and coral"></div>
    <div class="pattern pattern--accent" role="img" aria-label="Small coral geometric triangle accent"></div>

    <svg class="pattern pattern--lower" viewBox="0 0 636 600" role="img" aria-label="Geometric pattern of red, coral, wine and lavender triangles">
      <defs>
        <linearGradient id="lower-fill" x1="0" y1="0" x2="0.6" y2="1">
          <stop offset="0" stop-color="#ef6a55" stop-opacity="0.75"/>
          <stop offset="0.45" stop-color="#c8202c"/>
          <stop offset="1" stop-color="#9e1f26"/>
        </linearGradient>
        <linearGradient id="lower-tint" x1="1" y1="0.3" x2="0.4" y2="1">
          <stop offset="0" stop-color="#9fa6d4" stop-opacity="0.7"/>
          <stop offset="0.6" stop-color="#9fa6d4" stop-opacity="0"/>
        </linearGradient>
      </defs>
      <polygon points="0,60 160,130 330,40 460,0 636,70 636,600 0,600" fill="url(#lower-fill)"/>
      <polygon points="0,60 160,130 330,40 460,0 636,70 636,600 0,600" fill="url(#lower-tint)"/>
    </svg>

    <h1 class="title">
      <span class="title__lead">Muddling</span>
      <span class="title__main">Through</span>
      <span class="title__sub">Small Years!</span>
    </h1>

    <div class="tagline-panel">
      <svg viewBox="0 0 400 300" aria-hidden="true">
        <polygon points="90,10 310,10 395,150 310,290 90,290 5,150" fill="var(--panel-fill)" stroke="var(--panel-edge)" stroke-width="3"/>
      </svg>
      <p class="tagline">Tips and ideas for 8 to 13 year olds about how to stay cool, calm and confident on even the toughest days!</p>
    </div>

    <div class="author-band">
      <span class="author-band__name">Maren Holloway</span>
      <span class="author-band__role">Clinical psychologist</span>
    </div>
    <p class="illustrator">Illustrated by: Tomas R. Vidal</p>
  </main>
</body>
</html>
```